Brand Business Card for Hotel Cloud Management System

Hello designers,
we are looking for a new brand business card for our product Roomvanta. Our brand Roomvanta is a hotel management system for small hotels, B&B, guesthouses etc. and just recently we are expanding our offer to other European markets. Therefore we need a business card that will communicate not only to the end-users (hoteliers) but also to potential business partners/ We would like the brand business card to be professional looking, but not too serius, modern, elegant, clean, Our brand color is orange, dark grey and it would be nice to see both combined.

Please visit our website www.roomvanta-example.eu to get more impression on what our brand roomvanta stands for.

Please find attached roomvanta logo.

Target Market(s)

small hotels, hoteliers, B&B owners, potential business partners

Industry/Entity Type

Software Service

Contact Information for Business Card

Roomvanta
- hotel software solutions - web booking engine - multi channel manager
www.roomvanta-example.eu
T: +38614007300
E: info@roomvanta-example.net

Font styles to use
Serif
Sans Serif

Colors
f37122
aaaaaa
606060
f6f6f6

Requirements
Must have
• Logo of the brand
• the layout of the business card should be in connection with the look and feel of the website roomvanta-example.eu and logo roomvanta;

```html
<!DOCTYPE html>
<html lang="en">
<head>
<meta charset="utf-8">
<title>Roomvanta business card</title>
<link rel="stylesheet" href="https://fonts.googleapis.com/css2?family=Quicksand:wght@400;500;700&display=swap">
<style>
  :root {
    --stage: #6a6a6c;
    --card: #1c1c1c;
    --card-texture: #232323;
    --orange: #f37122;
    --white: #f6f6f6;
    --grey: #aaaaaa;
  }
  * { margin: 0; padding: 0; box-sizing: border-box; }
  html, body { width: 1200px; height: 913px; overflow: hidden; }
  body {
    background: var(--stage);
    font-family: "Quicksand", sans-serif;
    position: relative;
  }
  .card {
    position: absolute;
    top: 190px;
    width: 340px;
    height: 530px;
    background: var(--card);
    border-radius: 4px;
    box-shadow: 0 14px 30px rgba(0,0,0,.35);
    overflow: hidden;
  }
  .card--front { left: 215px; }
  .card--back { left: 645px; }
  .card-texture {
    position: absolute; inset: 0;
    background: linear-gradient(160deg, var(--card-texture), var(--card) 70%);
  }
  .front-brand {
    position: absolute; left: 0; right: 0; top: 210px;
    display: flex; align-items: center; justify-content: center; gap: 14px;
  }
  .brand-square {
    width: 44px; height: 44px; border-radius: 8px; background: var(--orange);
  }
  .front-name {
    font-size: 46px; font-weight: 700; color: var(--white); letter-spacing: .5px;
  }
  .back-content {
    position: absolute; left: 0; right: 0; top: 95px;
    text-align: center; color: var(--white);
  }
  .back-name {
    display: flex; align-items: center; justify-content: center; gap: 10px;
    font-size: 42px; font-weight: 700; line-height: 1;
  }
  .back-name .brand-square { width: 28px; height: 28px; border-radius: 6px; }
  .tagline {
    margin-top: 6px; font-size: 14px; font-weight: 500; color: var(--grey); letter-spacing: 1px;
  }
  .rule {
    width: 22px; height: 2px; background: var(--orange); margin: 24px auto;
  }
  .services { list-style: none; font-size: 13px; font-weight: 700; line-height: 1.5; letter-spacing: .5px; }
  .contact {
    list-style: none; font-size: 13px; font-weight: 500; line-height: 1.6;
    width: max-content; margin: 0 auto; text-align: left; color: var(--grey);
  }
  .contact .label { color: var(--orange); font-weight: 700; }
</style>
</head>
<body>
  <section class="card card--front" aria-label="Card front">
    <div class="card-texture" role="img" aria-label="Subtle dark woven background pattern"></div>
    <div class="front-brand">
      <span class="brand-square"></span>
      <span class="front-name">Roomvanta</span>
    </div>
  </section>

  <section class="card card--back" aria-label="Card back">
    <div class="card-texture" role="img" aria-label="Subtle dark woven background pattern"></div>
    <div class="back-content">
      <div class="back-name"><span class="brand-square"></span><span>Roomvanta</span></div>
      <p class="tagline">hotel pms service</p>
      <div class="rule"></div>
      <ul class="services">
        <li>hotel software solutions</li>
        <li>web booking engine</li>
        <li>multi channel manager</li>
      </ul>
      <div class="rule"></div>
      <ul class="contact">
        <li><span class="label">W:</span> www.roomvanta-example.eu</li>
        <li><span class="label">T:</span> +38614007300</li>
        <li><span class="label">E:</span> info@roomvanta-example.net</li>
      </ul>
    </div>
  </section>
</body>
</html>
```